Creative UI design for web application

I need a new UI design for my web application. It will be used by small and micro business owners to plan & implement growth tactics.

I've attached the current design (which I'm open to be changed) - but in particular I need to design the centre of the screen, where the work actually happens.

There needs to be place for a title (YOUR BUSINESS) and description (say 1-2 paragraphs of text) - and am happy to include icons or imagery where makes sense. It may make sense for the user to be able to upload their business logo and name, for example.

This screen will be used by the business owner to understand the real value they offer potential customers and their point of difference - why they exist and why potential customers should care.

They'll use the information they put into this screen to plan things like their messaging.

Following that, there needs to be 2 sections in the dashboard.

The first section is titled "WHO YOU ARE"

The first section will include a number of boxes that the user can input information into, as follows:

- Logo
- Business name
- Business tag line
- Business vision
- Business bio
- Brand colours (these should end up as swatches based on the colour code they enter) - the colour code for each colour swatch should also be visible.
- Key competitors
- SWOT analysis (boxes to enter their strengths, weaknesses, opportunities and threats).

The second section is titled "WHY YOU EXIST"

The second section will include a number of boxes that the user can input information (text) into, as follows:

- Who are your ideal customers?
- What problem are you trying to solve for them?
- What pain points will this remove for them?
- How do you solve it?
- How else could this problem be solved?
- Who offers these other solutions?
- Why is your solution better?
- How much does your solution cost?
- What value are you providing to justify this cost?
- How will this make their life/job easier/better?

They should be able to write a decent amount of information in the boxes.

There should ideally be a place for a description for each of these text fields (for both section 1 & 2) as well so I can give them a little bit more direction around what to put in the box. Alternatively there could be a little icon (say a question mark or "i") that they could click on to view instructions. The instructions will be around 2-4 sentences long for each text field.

You have 2 options:

a) This all needs to appear on the one screen, and the navigation needs to be visible (as per the example attached but feel free to recreate this navigation)

Note: the page can scroll below the fold - but please provide the design for the full length of the page.

b) Potentially the 2 sections could actually be in 2 different items in the menu - YOUR BUSINESS and YOUR VALUE (which would sit next to YOUR BUSINESS and before YOUR CUSTOMER in the screenshot provided). feel free to design them as 2 separate screens if you prefer.

I have attached a screenshot of the app as it stands today (screen shot 2017) which would still exist in the new design but under a different section (the learn section from the plan2 mockup attached)

I have mocked up how this new screen could look if broken into 2 and that's also attached. If you can make this come to life - and look more engaging that would be helpful! :)

Target Market(s)

Small and micro business owners

Industry/Entity Type

Marketing

Number of Pages Required

1 page

Font styles to use
Sans Serif
Other font styles liked:
• Montserrat

Colors
87cfc6
d2a4cc
ffffff
85cae6
e8e8e8
5c5c5c

Requirements
Must have
• Use of my brand colours: #cc8eb2, #76d6c8, #68c7ff as well as white and #595959. Must be visually pleasing / engaging, designed for desktop (as it's a desktop application), really easy to use / navigate.
• Use font Montserrat light & Montserrat Regular or Bold. Mostly should be Montserrat light.
Nice to have
• Would be nice to see how this would look on mobile (as the application is responsive) but this is not mandatory.
Should not have
• Should not look too corporate or dry.

```html
<!DOCTYPE html>
<html lang="en">
<head>
<meta charset="utf-8">
<title>Your Business – Who You Are</title>
<link href="https://fonts.googleapis.com/css2?family=Montserrat:wght@300;400;500;700&display=swap" rel="stylesheet">
<style>
  :root {
    --bar-dark: #575757;
    --bar-mid: #808080;
    --mint: #87cfc6;
    --pink: #d2a4cc;
    --sky: #85cae6;
    --page: #e8e8e8;
    --ink: #5c5c5c;
    --line: #dedede;
    --muted: #808080;
    --placeholder: #dcdcdc;
    --white: #ffffff;
  }
  * { box-sizing: border-box; margin: 0; padding: 0; }
  html, body { width: 1200px; height: 675px; overflow: hidden; }
  body {
    position: relative;
    background: var(--page);
    font-family: "Montserrat", sans-serif;
    font-weight: 300;
    color: var(--ink);
  }
  .abs { position: absolute; }

  /* top navigation */
  .main-nav { left: 0; top: 0; width: 1200px; height: 37px; background: var(--bar-dark); }
  .brand { left: 17px; top: 0; height: 37px; line-height: 44px; font-size: 15px; font-weight: 400; color: var(--white); }
  .main-nav__item { top: 0; height: 37px; line-height: 45px; font-size: 14.5px; font-weight: 400; color: var(--white); }
  .main-nav__item--active { background: var(--mint); text-align: center; }

  .sub-nav { left: 0; top: 37px; width: 1200px; height: 44px; background: var(--bar-mid); }
  .sub-nav__item { top: 0; height: 44px; line-height: 46px; font-size: 14.5px; font-weight: 400; color: var(--white); }
  .sub-nav__item--active { background: var(--pink); text-align: center; }

  /* section heading */
  .section-marker { left: 13px; top: 104px; width: 25px; height: 18px; background: var(--sky); }
  .section-title { left: 44px; top: 101px; font-size: 19px; font-weight: 700; color: var(--ink); letter-spacing: -0.3px; }

  /* cards */
  .card { top: 139px; height: 484px; width: 575px; background: var(--white); border: 1px solid var(--sky); }
  .card::before { content: ""; position: absolute; left: 0; top: 0; bottom: 0; width: 25px; background: var(--sky); }
  .card--identity { left: 13px; }
  .card--colours { left: 613px; }

  .tile { border: 1px solid var(--line); background: var(--white); text-align: center; font-size: 11px; line-height: 13.5px; color: var(--muted); }
  .tile svg { display: block; margin: 12px auto 9px; }

  .field-label { font-size: 14.5px; font-weight: 300; color: var(--ink); }
  .field { border: 1px solid var(--line); background: var(--white); }
  .field--placeholder { padding-left: 13px; line-height: 36px; font-size: 14.5px; color: var(--placeholder); }

  .hint { font-size: 10.5px; color: var(--ink); display: flex; align-items: center; gap: 6px; }
  .btn-add { background: var(--sky); color: var(--white); font-size: 11.5px; text-align: center; line-height: 37px; }

  .swatches { left: 662px; top: 333px; width: 500px; display: grid; grid-template-columns: repeat(4, 125px); grid-auto-rows: 125px; }
  .swatch { display: flex; align-items: center; justify-content: center; font-size: 14.5px; font-weight: 500; color: var(--white); }
</style>
</head>
<body>

  <header class="abs main-nav">
    <div class="abs brand">BLOOMPATH</div>
    <div class="abs main-nav__item main-nav__item--active" style="left:160px;width:75px;">Plan</div>
    <div class="abs main-nav__item" style="left:258px;">Learn</div>
    <div class="abs main-nav__item" style="left:331px;">Remember</div>
  </header>

  <nav class="abs sub-nav">
    <div class="abs sub-nav__item sub-nav__item--active" style="left:147px;width:138px;">Your Business</div>
    <div class="abs sub-nav__item" style="left:316px;">Your Value</div>
    <div class="abs sub-nav__item" style="left:441px;">Your Customers</div>
    <div class="abs sub-nav__item" style="left:612px;">Your Goals</div>
    <div class="abs sub-nav__item" style="left:742px;">Your Plan</div>
  </nav>

  <div class="abs section-marker"></div>
  <h1 class="abs section-title">WHO YOU ARE</h1>

  <section class="abs card card--identity"></section>
  <section class="abs card card--colours"></section>

  <!-- identity fields -->
  <div class="abs tile" style="left:62px;top:164px;width:132px;height:131px;">
    <svg width="64" height="64" viewBox="0 0 64 64" fill="none" stroke="#e6e6e6" stroke-width="7" stroke-linejoin="round">
      <path d="M4 22V4h18M42 4h18v18M60 42v18H42M22 60H4V42"/>
    </svg>
    Upload your<br>business logo
  </div>

  <label class="abs field-label" style="left:211px;top:160px;">Business name</label>
  <div class="abs field" style="left:212px;top:184px;width:350px;height:37px;"></div>

  <label class="abs field-label" style="left:211px;top:233px;">Business tag line</label>
  <div class="abs field" style="left:212px;top:258px;width:350px;height:37px;"></div>

  <label class="abs field-label" style="left:61px;top:310px;">Business vision</label>
  <div class="abs field" style="left:62px;top:334px;width:500px;height:113px;"></div>

  <label class="abs field-label" style="left:61px;top:461px;">Business bio</label>
  <div class="abs field" style="left:62px;top:486px;width:500px;height:113px;"></div>

  <!-- colour fields -->
  <div class="abs tile" style="left:662px;top:164px;width:132px;height:131px;">
    <svg width="64" height="66" viewBox="0 0 64 66" fill="none" stroke="#e2e2e2" stroke-width="3" stroke-linejoin="round">
      <rect x="41" y="3" width="12" height="20" rx="6" transform="rotate(45 47 13)"/>
      <path d="M36 18l10 10M40 24L16 48l-4 0 0-4L36 20"/>
      <path d="M9 52c-3 5-4 7-4 9a4 4 0 0 0 8 0c0-2-1-4-4-9z"/>
    </svg>
    Chooser your<br>business colors
  </div>

  <label class="abs field-label" style="left:811px;top:160px;">Business colours</label>
  <div class="abs field field--placeholder" style="left:813px;top:184px;width:350px;height:37px;">#87cfc6</div>

  <p class="abs hint" style="left:812px;top:233px;">
    <svg width="13" height="13" viewBox="0 0 13 13" fill="none" stroke="#5c5c5c" stroke-width="1">
      <circle cx="6.5" cy="6.5" r="5.8"/><path d="M6.5 5.5v4M6.5 3.4v0.8"/>
    </svg>
    Paste hexadecimal color codes or use color picker
  </p>

  <div class="abs btn-add" style="left:813px;top:258px;width:125px;height:37px;">ADD</div>

  <div class="abs swatches">
    <div class="swatch" style="background:#3498db;">#3498DB</div>
    <div class="swatch" style="background:#9b59b6;">#9B59B6</div>
    <div class="swatch" style="background:#34495e;">#34495E</div>
    <div class="swatch" style="background:#ecf0f1;color:#5c5c5c;">#ECF0F1</div>
    <div class="swatch" style="background:#2980b9;">#2980B9</div>
    <div class="swatch" style="background:#f1c40f;">#F39C12</div>
    <div class="swatch" style="background:#e74c3c;">#E74C3C</div>
  </div>

</body>
</html>
```